Brantley Advisory Group provides support for renewable energy projects to utilities and suppliers

I need a professional looking business card that is both simple and elegant and unique. My clients are mostly large organizations not individuals. I am a consultant with my own company that is small but would like to give clients the impression I am larger. Smart grid, fiber optics, software, field hardware, distribution automation, substation automation, operations, energy storage/batteries, microgrids, customer service, strategy/roadmaps, conservation, Automated Metering Infrastruture (AMI or smart meters) are all areas of focus.

Target Market(s)

Utilities, suppliers, governmental agencies involved in energy. All types of energy especially natural gas and electrical. Especially renewable energy or green projects.

Contact Information for Business Card

Name - Mark Brantley Cell Phone - 425.318.2746 Email - mbrantley@brantleyag-example.com
Company - Brantley Advisory Group (logo) Title - Principal

Font styles to use
Serif
Sans Serif

Colors

Designer to choose colors to be used in the design.

Requirements
Must have
• Simple and professional and powerful.
• Unique/creative design.
Nice to have
• Utilize color scheme to accent logo colors. Maybe some geometric pattern on edge of card with color.
Should not have
• Busy, complicated, traditional

```html
<!DOCTYPE html>
<html lang="en">
<head>
<meta charset="utf-8">
<title>Brantley Advisory Group — Business Card</title>
<link rel="stylesheet" href="https://fonts.googleapis.com/css2?family=Lora:wght@400&family=Varela+Round&display=swap">
<style>
  :root {
    --backdrop: #8e8c8c;
    --card-dark: #282625;
    --card-green: #668f3e;
    --card-green-light: #80ab52;
    --brand-green: #6e9a45;
    --name-blue: #7f86d6;
    --detail-grey: #a09c98;
    --white: #ffffff;
  }
  * { box-sizing: border-box; margin: 0; padding: 0; }
  html, body {
    width: 1200px; height: 900px; overflow: hidden;
    background: var(--backdrop);
  }
  .canvas { position: relative; width: 1200px; height: 900px; }

  .card {
    position: absolute;
    width: 560px; height: 320px;
    border-radius: 22px;
    box-shadow: 0 6px 14px rgba(0,0,0,0.25);
    overflow: hidden;
  }

  /* Front: contact side */
  .card-front { left: 90px; top: 110px; background: var(--card-dark); }
  .front-brand {
    position: absolute; top: 34px; right: 36px;
    display: flex; align-items: center; gap: 12px;
  }
  .brand-square {
    width: 30px; height: 30px;
    border: 2px solid var(--brand-green); border-radius: 4px;
  }
  .brand-name {
    font-family: "Varela Round", sans-serif;
    font-size: 20px; color: var(--brand-green);
    line-height: 1.15;
  }
  .contact-block {
    position: absolute; left: 40px; bottom: 36px;
    font-family: "Lora", serif;
  }
  .person-name { font-size: 26px; color: var(--name-blue); line-height: 1.1; }
  .person-title { font-size: 20px; color: var(--brand-green); margin-bottom: 22px; }
  .contact-line {
    display: flex; align-items: center; gap: 10px;
    font-size: 15px; color: var(--detail-grey); letter-spacing: 0.5px;
    margin-top: 6px; margin-left: 30px;
  }
  .contact-icon { width: 16px; height: 14px; flex: none; }

  /* Back: brand side */
  .card-back {
    left: 550px; top: 470px;
    background: linear-gradient(125deg, var(--card-green) 0%, var(--card-green-light) 30%, var(--card-green) 55%);
  }
  .back-brand {
    position: absolute; inset: 0;
    display: flex; align-items: center; justify-content: center; gap: 22px;
  }
  .back-brand .brand-square {
    width: 70px; height: 70px; border: 3px solid var(--white); border-radius: 8px;
  }
  .back-brand .brand-name { color: var(--white); font-size: 38px; }
</style>
</head>
<body>
<main class="canvas">
  <section class="card card-front" aria-label="Business card, contact side">
    <div class="front-brand">
      <span class="brand-square" aria-hidden="true"></span>
      <span class="brand-name">Brantley<br>Advisory Group</span>
    </div>
    <div class="contact-block">
      <p class="person-name">Mark Brantley</p>
      <p class="person-title">owner</p>
      <p class="contact-line">
        <svg class="contact-icon" viewBox="0 0 16 14" aria-hidden="true">
          <path d="M1 5 Q8 0 15 5 L13 7 L11 5 L5 5 L3 7 Z" fill="#6e9a45"/>
          <rect x="3" y="7" width="10" height="6" rx="1" fill="#6e9a45"/>
        </svg>
        +425.318.2746
      </p>
      <p class="contact-line">
        <svg class="contact-icon" viewBox="0 0 16 14" aria-hidden="true">
          <rect x="1" y="2" width="14" height="10" fill="#6e9a45"/>
          <path d="M1 2 L8 8 L15 2" fill="none" stroke="#282625" stroke-width="1.2"/>
        </svg>
        mbrantley@brantleyag-example.com
      </p>
    </div>
  </section>

  <section class="card card-back" aria-label="Business card, brand side">
    <div class="back-brand">
      <span class="brand-square" aria-hidden="true"></span>
      <span class="brand-name">Brantley<br>Advisory Group</span>
    </div>
  </section>
</main>
</body>
</html>
```